Re-Design an adult education portal

I need support to re-design an adult education portal. Currently the customer has an incomplete website which should be prepared in a new format.
I have the idea how to realize, but I have no clue how to design it. The hard thing is to have a "beautiful" website with available logo and main color. I hope you can support me.

Name of Website: tovrenu (tovrenu.ch)
Content: adult eduction for adult in safety at work, mountain climbing, dog school. various courses in different areas. But on old webpage is hard to find the different possibilities.
main color: Ral 6011 (green) -> #6C7C59
logo: you see on top of website the logo (2 dogs and a mountain with a colour gradient).

new website: for new webpage I decided to have a navigation for each section of education. In the main area I would like to have some pictures to give an idea what content is behind. At the moment it looks terrible, so I decided to use you as support for me to make the webpage prettier :). And maybe you have an better idea how to make it great. -> current state of new web page: https://tovrenu.bask-om.ch/

Target Market(s)

adult eduction for adult in safety at work, mountain climbing, dog school

Number of Pages Required

1 page

Font styles to use
Serif
Sans Serif

Requirements
Must have
• As main color is set "Ral 6011" (green) -> #6C7C59

```html
<!DOCTYPE html>
<html lang="en">
<head>
<meta charset="utf-8">
<title>tovrenu – Training &amp; Course Partner</title>
<link rel="stylesheet" href="https://fonts.googleapis.com/css2?family=Lato:wght@400;700;900&family=Merriweather:wght@700&display=swap">
<style>
:root{
  --green:#6c7c59;
  --green-dark:#55633f;
  --ink:#1b1b1b;
  --text:#444;
  --grey-band:#ececec;
  --white:#fff;
  --footer:#141414;
}
*{box-sizing:border-box;margin:0;padding:0}
html,body{width:1200px;height:3704px;overflow:hidden}
body{position:relative;background:var(--white);font-family:"Lato",sans-serif;color:var(--text)}
.abs{position:absolute}
.btn{display:inline-block;border-radius:30px;font:700 13px "Lato",sans-serif;letter-spacing:.5px;text-transform:uppercase;color:var(--white);background:var(--ink);padding:10px 28px;text-align:center}
.btn-green{background:var(--green)}

/* hero */
.hero{left:0;top:0;width:1200px;height:880px;clip-path:polygon(0 0,100% 0,100% 790px,0 880px);
  background:linear-gradient(180deg,#9fb0bf 0%,#6e7a5a 30%,#4d5436 60%,#3d3a2b 100%)}
.hero-photo{position:absolute;inset:0;background:radial-gradient(ellipse at 50% 55%,rgba(160,120,80,.35),rgba(0,0,0,.35) 70%)}
.logo{left:22px;top:14px;width:160px;height:104px;background:rgba(255,255,255,.85);display:flex;align-items:center;justify-content:center;gap:8px}
.logo-mark{width:14px;height:14px;border-radius:50%;background:var(--green)}
.logo-name{font:900 24px "Lato",sans-serif;color:var(--green)}
.nav{left:488px;top:40px;display:flex;gap:8px;align-items:center}
.nav a{font:700 13px "Lato",sans-serif;color:var(--white);text-decoration:none;padding:8px 18px;border-radius:20px;text-transform:uppercase}
.nav a.active{background:var(--green)}
.hero-title{left:0;width:1200px;top:440px;text-align:center;font:700 54px "Merriweather",serif;color:var(--white);text-shadow:0 2px 8px rgba(0,0,0,.4)}
.hero-sub{left:300px;width:600px;top:515px;text-align:center;font:700 22px/1.45 "Lato",sans-serif;color:var(--white)}
.hero-btn{left:533px;top:608px}

/* about */
.about-photo{left:72px;top:1000px;width:608px;height:400px;background:linear-gradient(160deg,#7f9a5e,#4f6b3a 55%,#8c6a4c)}
.about-card{left:520px;top:1032px;width:612px;height:368px;background:var(--white);box-shadow:0 6px 24px rgba(0,0,0,.18);padding:34px 36px}
.about-card h2{font:700 34px "Lato",sans-serif;color:var(--ink);margin-bottom:14px}
.about-card p{font:400 17px/1.75 "Lato",sans-serif;color:var(--text)}
.about-card .btn{margin-top:18px}

/* training */
.training{left:0;top:1480px;width:1200px;height:880px;background:var(--grey-band);clip-path:polygon(0 100px,100% 0,100% 780px,0 880px)}
.section-title{left:0;width:1200px;text-align:center;font:700 36px "Lato",sans-serif;color:var(--ink);letter-spacing:1px;text-transform:uppercase}
.tabs{left:0;width:1200px;top:1698px;display:flex;justify-content:center;gap:24px}
.tabs span{font:700 13px "Lato",sans-serif;color:var(--ink);padding:8px 20px;border-radius:20px;text-transform:uppercase}
.tabs span.active{background:var(--green);color:var(--white)}
.course-grid{left:72px;top:1760px;display:grid;grid-template-columns:repeat(4,252px);gap:16px}
.course-card{background:var(--white);height:400px;text-align:center;box-shadow:0 3px 10px rgba(0,0,0,.08)}
.course-img{height:200px}
.course-card h3{font:900 15px/1.3 "Lato",sans-serif;color:var(--ink);text-transform:uppercase;margin:20px 16px 10px;height:40px;display:flex;align-items:center;justify-content:center}
.course-card p{font:400 13px/1.5 "Lato",sans-serif;color:var(--text);margin:0 24px 16px}

/* team */
.team-grid{left:184px;top:2410px;display:grid;grid-template-columns:repeat(3,296px);gap:28px}
.team-card{text-align:center}
.team-img{height:240px}
.team-card h3{font:900 16px "Lato",sans-serif;color:var(--ink);text-transform:uppercase;margin:28px 0 18px}
.arrow{top:2548px}

/* contact */
.contact{left:0;top:2790px;width:1200px;height:700px;clip-path:polygon(0 70px,100% 0,100% 100%,0 100%);
  background:linear-gradient(160deg,#4a5a3c 0%,#2d3427 45%,#1d211a 100%)}
.contact-title{color:var(--white);top:2950px}
.field{position:absolute;background:var(--white);border-radius:28px;font:400 16px "Lato",sans-serif;color:#555;padding:0 26px;display:flex;align-items:center}
.info{left:76px;display:flex;gap:22px;align-items:center;color:var(--white)}
.info-icon{width:56px;height:56px;border-radius:50%;border:2px solid var(--white);display:flex;align-items:center;justify-content:center}
.info h4{font:900 15px "Lato",sans-serif;text-transform:uppercase}
.info p{font:400 16px/1.4 "Lato",sans-serif}

/* footer */
.footer{left:0;top:3490px;width:1200px;height:214px;background:var(--footer)}
.footer-nav{left:0;width:1200px;top:3538px;display:flex;justify-content:center;gap:48px}
.footer-nav a{font:700 14px "Lato",sans-serif;color:var(--white);text-decoration:none;text-transform:uppercase}
.copyright{left:0;width:1200px;top:3582px;text-align:center;font:400 14px "Lato",sans-serif;color:#ccc}
.socials{left:0;width:1200px;top:3622px;display:flex;justify-content:center;gap:20px}
.socials span{width:22px;height:22px;border-radius:50%;background:var(--white)}
</style>
</head>
<body>

<section class="abs hero" role="img" aria-label="Photo of the two trainers with their dogs outdoors under a tree"><div class="hero-photo"></div></section>
<div class="abs logo"><span class="logo-mark"></span><span class="logo-name">tovrenu.ch</span></div>
<nav class="abs nav">
  <a class="active">Home</a><a>About Us</a><a>Training Courses</a><a>Team</a><a>Contact Us</a>
</nav>
<h1 class="abs hero-title">Your Training &amp; Course Partner</h1>
<p class="abs hero-sub">We offer training tailored to your needs, target-oriented and tailored to your skills and knowledge.</p>
<a class="abs btn btn-green hero-btn">Read More</a>

<div class="abs about-photo" role="img" aria-label="Photo of the trainers sitting in a meadow with two dogs"></div>
<section class="abs about-card">
  <h2>ABOUT TOVRENU</h2>
  <p>In my professional career, I have repeatedly experienced situations that gave me the idea of giving every interested person basic knowledge that would allow them to react correctly and with the necessary calm in an emergency. The pooling and combining of knowledge and skills from the various specialist areas gives people security and confidence in their actions.</p>
  <a class="btn">Read More</a>
</section>

<section class="abs training"></section>
<h2 class="abs section-title" style="top:1620px">Training &amp; Course</h2>
<div class="abs tabs">
  <span class="active">Occupational Safety</span><span>First Aid</span><span>Dog School</span><span>CZV</span><span>Mountain Training</span>
</div>
<div class="abs course-grid">
  <article class="course-card"><div class="course-img" role="img" aria-label="Photo of an orange forklift in a warehouse" style="background:linear-gradient(150deg,#c9a46a,#e07a1f 50%,#6b5a44)"></div><h3>Forklift Courses</h3><p>Sed ut perspiciatis unde omnis natus error sit voluptatem</p><a class="btn">Read More</a></article>
  <article class="course-card"><div class="course-img" role="img" aria-label="Photo of fall-protection harness and helmet equipment" style="background:linear-gradient(150deg,#d9b24a,#c4532a 55%,#7a4b2c)"></div><h3>Personal Protective Equipment Against Falls</h3><p>Sed ut perspiciatis unde omnis natus error sit voluptatem</p><a class="btn">Read More</a></article>
  <article class="course-card"><div class="course-img" role="img" aria-label="Photo of a red aerial work platform vehicle" style="background:linear-gradient(160deg,#9fb6cc,#8a8d86 50%,#a8332a)"></div><h3>Aerial Work Platform</h3><p>Sed ut perspiciatis unde omnis natus error sit voluptatem</p><a class="btn">Read More</a></article>
  <article class="course-card"><div class="course-img" role="img" aria-label="Photo of a technician working in a laboratory" style="background:linear-gradient(150deg,#dfe4ea,#9fb3c8 60%,#5d6f86)"></div><h3>Material Control</h3><p>Sed ut perspiciatis unde omnis natus error sit voluptatem</p><a class="btn">Read More</a></article>
</div>

<h2 class="abs section-title" style="top:2330px">Team</h2>
<svg class="abs arrow" style="left:40px" width="24" height="40" viewBox="0 0 24 40"><path d="M18 4 4 20l14 16" fill="none" stroke="#222" stroke-width="3"/></svg>
<svg class="abs arrow" style="left:1136px" width="24" height="40" viewBox="0 0 24 40"><path d="M6 4l14 16L6 36" fill="none" stroke="#222" stroke-width="3"/></svg>
<div class="abs team-grid">
  <article class="team-card"><div class="team-img" role="img" aria-label="Portrait photo of Lukas Vernier in the mountains" style="background:linear-gradient(170deg,#b9cde0,#8fa2b4 50%,#5d6470)"></div><h3>Lukas Vernier</h3><a class="btn">Read More</a></article>
  <article class="team-card"><div class="team-img" role="img" aria-label="Photo of Anna Vernier climbing in a red jacket" style="background:linear-gradient(170deg,#8fb0d4,#c0472c 55%,#4d5a3c)"></div><h3>Anna Vernier</h3><a class="btn">Read More</a></article>
  <article class="team-card"><div class="team-img" role="img" aria-label="Photo of the dog Bruno on grass" style="background:linear-gradient(170deg,#7c9a5a,#3a2d22 55%,#5f7a40)"></div><h3>Bruno</h3><a class="btn">Read More</a></article>
</div>

<section class="abs contact" role="img" aria-label="Dark photo backdrop with a climber standing on a ladder"></section>
<h2 class="abs section-title contact-title">Contact Us</h2>
<div class="field" style="left:432px;top:3024px;width:336px;height:56px">First Name</div>
<div class="field" style="left:792px;top:3024px;width:336px;height:56px">Last Name</div>
<div class="field" style="left:432px;top:3092px;width:336px;height:56px">Phone No</div>
<div class="field" style="left:792px;top:3092px;width:336px;height:56px">Email Address</div>
<div class="field" style="left:432px;top:3166px;width:696px;height:146px;align-items:flex-start;padding-top:16px;border-radius:20px">Message</div>
<a class="abs btn" style="left:432px;top:3326px;width:330px;height:56px;line-height:36px;font-size:16px">Submit</a>

<div class="abs info" style="top:3074px">
  <div class="info-icon"><svg width="24" height="24" viewBox="0 0 24 24"><path d="M12 2a7 7 0 0 0-7 7c0 5 7 13 7 13s7-8 7-13a7 7 0 0 0-7-7zm0 9.5A2.5 2.5 0 1 1 12 6.5a2.5 2.5 0 0 1 0 5z" fill="#fff"/></svg></div>
  <div><h4>Address</h4><p>Talweg 21<br>3999 Oberdorf</p></div>
</div>
<div class="abs info" style="top:3176px">
  <div class="info-icon"><svg width="24" height="24" viewBox="0 0 24 24"><path d="M6.6 10.8a15 15 0 0 0 6.6 6.6l2.2-2.2a1 1 0 0 1 1-.25 11.4 11.4 0 0 0 3.6.57 1 1 0 0 1 1 1V20a1 1 0 0 1-1 1A17 17 0 0 1 3 4a1 1 0 0 1 1-1h3.5a1 1 0 0 1 1 1c0 1.25.2 2.45.57 3.57a1 1 0 0 1-.25 1z" fill="#fff"/></svg></div>
  <div><h4>Phone</h4><p>+41 79 000 12 34</p></div>
</div>
<div class="abs info" style="top:3276px">
  <div class="info-icon"><svg width="24" height="24" viewBox="0 0 24 24"><rect x="3" y="5" width="18" height="14" rx="2" fill="none" stroke="#fff" stroke-width="2"/><path d="M3 7l9 6 9-6" fill="none" stroke="#fff" stroke-width="2"/></svg></div>
  <div><h4>Email</h4><p>info@tovrenu.ch</p></div>
</div>

<footer class="abs footer"></footer>
<nav class="abs footer-nav"><a>Home</a><a>About Us</a><a>Training Courses</a><a>Team</a><a>Contact Us</a></nav>
<p class="abs copyright">Copyright © 2021. Company Name All rights reserved.</p>
<div class="abs socials"><span></span><span></span><span></span><span></span><span></span></div>

</body>
</html>
```